Rice Cakes Packing Desing

We need a simple (4 color) yet colorful, atractive design for a Rice Cake polypropylene bag. We are expanding our line to include 8-10 different flavors with each bag being a different color for easy identificaction. We are starting right with the first design. We already have "sample model" (of an existing product in the usa market) upon which we believe that our design could be based on (as an idea of a simple 4 color plastic bag design), which we are including in this post. We are also including an image of Brindle Rice Cakes plastic bag that has a round front window that shows the product inside the bag, which we also would like to include in our design. We already have a brand name and a logo design. The bag's dimension is about 20cms (wide) 30cms (tall) and it will contain about 12 rice cakes inside. (I HAVE ATTACHED A COUPLE OF IMAGES OF A PRINTED POLYPROPYLENE RICE CAKES BAG FOR YOUR REFERENCE)
Updates

Project Deadline Extended
Reason: We want to provide the designers with NUTRITIONAL INFORMATION, Bar Code, Company information, Ingredients, important pointers, etc. to be incorporated into the design. We would like to provide a few more days in order to fully integrate the back & front text into the package design in order to attain a perfectly balanced and well presented package. So far we have received some very interesting and highly viable proposals and we would like to provide the designers the necessary text information in order to have a complete, fully designed, great-looking package. We feel that with the extension the final design can be completed and we can have an opportunity to review, incorporate/change/modify any details before choosing the final design. Great designs have been submitted and we will definitely choose one before the newly proposed deadline. Thanks to all!

Target Market(s)

Although the concept of RICE CAKES might very well have its origins in ASIA the idea is to create a design (logo & pack) that will convey a message to the end consumer that our brand name stands for "FRESHNESS", "HEALTHY", "NATURE'S BEST", "TOP GRAINS", "GOODNESS", in short if you consume are products "IT IS GOOD FOR YOU!" (not only for people who love oriental food). We would like to have a product image that says "Hey! This looks Healthy & Tasty" (non-fattening, yummy and good!)

When you buy a pack of GRANOLAS what do you think about? What do you believe it is that you are buying? Good, Healthy Stuff? Good Tasting? Good for you? That's the idea!

Besides Rice Cakes are super light, fluffy, crunchy and easy to digest that it makes it a great Snack for everyone! Kids & Adults!

We need the full complete design of the actual bag (where the Rice Cakes will be packed) in order to start production of the bags right.

Industry/Entity Type

Plastic

Requirements
Must have
• We already have a local company in Mexico City that makes printed polypropylene bags. They are only waiting for the bag design in order to print the 20cms x 30cms bags.
Kindly consider that on the back Nutritional Information will be needed as well as a BarCode, company information, some bullets (pointing to the most important benefits of the product), etc. We will provide all the text information.
Nice to have
• Kindly take a look at the newly uploaded images from "VORNEP" Rice Cake packages. They are a good example of how to accomplish a great looking design using only 4 colors (which saves a lot in printing costs)
Should not have
• We do NOT want to have a design that says "This is ORIENTAL food". We don't want it to appear like "Sushi Rice" or "Japanese food", etc.

```html
<!DOCTYPE html>
<html lang="en">
<head>
<meta charset="utf-8">
<title>Ora Foods Rice Cakes – Bag Front</title>
<link href="https://fonts.googleapis.com/css2?family=Lilita+One&family=Oswald:wght@300;600&family=Poiret+One&display=swap" rel="stylesheet">
<style>
  :root {
    --bag-blue: #1b98d5;
    --sky-blue: #62c6ee;
    --grass-green: #3d9b2f;
    --leaf-green: #4caf3a;
    --paper: #ffffff;
    --seal-line: #e1e4e8;
  }
  html, body { margin: 0; padding: 0; overflow: hidden; background: var(--paper); }
  .bag {
    position: relative;
    width: 800px;
    height: 1200px;
    overflow: hidden;
    background: var(--paper);
  }
  .hang-tab {
    position: absolute; left: 133px; top: 0;
    width: 534px; height: 125px;
    background: var(--bag-blue);
  }
  .seal-lines { position: absolute; left: 0; top: 125px; width: 800px; height: 230px; }
  .bag-body {
    position: absolute; left: 0; top: 355px;
    width: 800px; height: 845px;
    background: var(--bag-blue);
  }
  .side-panel {
    position: absolute; top: 450px;
    width: 80px; height: 700px;
    background: var(--paper);
  }
  .side-panel--left { left: 0; border-radius: 0 26px 26px 0; }
  .side-panel--right { right: 0; border-radius: 26px 0 0 26px; }
  .tagline {
    position: absolute; left: 40px; top: 470px;
    width: 560px; height: 60px;
    transform-origin: 0 0;
    transform: rotate(90deg) translateY(-30px);
    font-family: "Poiret One", sans-serif;
    font-size: 50px; line-height: 60px;
    color: var(--grass-green);
    white-space: nowrap;
    font-weight: 700;
  }
  .heart-icon { position: absolute; left: 20px; top: 1060px; width: 40px; height: 40px; }
  .front-window {
    position: absolute; left: 139px; top: 400px;
    width: 522px; height: 800px;
    background: linear-gradient(180deg, var(--sky-blue) 0%, var(--sky-blue) 45%, #8cc63f 62%, var(--leaf-green) 85%, var(--grass-green) 100%);
  }
  .brand-mark {
    position: absolute; left: 280px; top: 405px;
    width: 240px; height: 140px;
    background: var(--grass-green);
    display: flex; align-items: center; justify-content: center;
    font-family: "Oswald", sans-serif; font-weight: 600;
    font-size: 40px; letter-spacing: 2px;
    color: var(--paper);
  }
  .product-name {
    position: absolute; left: 270px; top: 760px;
    width: 390px;
    margin: 0;
    text-align: center;
    font-family: "Lilita One", sans-serif;
    font-weight: 400;
    font-size: 128px; line-height: 110px;
    color: var(--paper);
    -webkit-text-stroke: 6px var(--grass-green);
    paint-order: stroke fill;
  }
  .flavour-band {
    position: absolute; left: 139px; top: 1080px;
    width: 522px; height: 56px;
    background: var(--paper);
    display: flex; align-items: center; justify-content: center;
    font-family: "Oswald", sans-serif; font-weight: 300;
    font-size: 40px; letter-spacing: 3px;
    color: var(--bag-blue);
  }
  .base-stripe {
    position: absolute; left: 139px; top: 1152px;
    width: 522px; height: 34px;
    background: var(--grass-green);
  }
</style>
</head>
<body>
<div class="bag">
  <div class="hang-tab"></div>
  <svg class="seal-lines" viewBox="0 0 800 230" aria-hidden="true">
    <g stroke="var(--seal-line)" stroke-width="10" fill="none">
      <line x1="-20" y1="40" x2="820" y2="-60"/>
      <line x1="-20" y1="120" x2="820" y2="20"/>
      <line x1="-20" y1="200" x2="820" y2="100"/>
      <line x1="-20" y1="280" x2="820" y2="180"/>
    </g>
  </svg>
  <div class="bag-body"></div>
  <div class="side-panel side-panel--left"></div>
  <div class="side-panel side-panel--right"></div>
  <div class="tagline">Naturally Healthy!</div>
  <svg class="heart-icon" viewBox="0 0 40 40" aria-hidden="true">
    <path d="M20 36 C6 26 2 18 2 12 C2 6 7 2 12 2 C16 2 19 5 20 8 C21 5 24 2 28 2 C33 2 38 6 38 12 C38 18 34 26 20 36 Z" fill="var(--grass-green)"/>
  </svg>
  <div class="front-window" role="img" aria-label="Sunny countryside scene: blue sky with a white cloud, rolling green hills and golden rice stalks"></div>
  <div class="brand-mark">ORA FOODS</div>
  <h1 class="product-name">RICE CAKES</h1>
  <div class="flavour-band">LIGHTLY SALTED</div>
  <div class="base-stripe"></div>
</div>
</body>
</html>
```